Dale Merrow Broker owner of Real Estate Company

Dale Merrow, GRI CRS ABR
Broker Owner
586-317-4902
dalemerrow@dalemerrowrealtors.example
14637 Larkspur Ave. St. Clair Shores, MI 48081
Licensed in Michigan and Florida
"37 Years of Outstanding Service based on a Result Driven Marketing Plan"

```html
<!DOCTYPE html>
<html lang="en">
<head>
<meta charset="utf-8">
<title>Dale Merrow — Business Card</title>
<link href="https://fonts.googleapis.com/css2?family=Arimo:wght@400;700&display=swap" rel="stylesheet">
<style>
  :root {
    --backdrop: #dfe0e2;
    --card: #f7f7f6;
    --maroon: #6a1f22;
    --maroon-band: #5e1c1f;
    --text-grey: #5b5b5b;
    --muted-grey: #8c8c8c;
    --portrait-top: #c9c2bd;
    --portrait-bottom: #2f3541;
  }
  * { box-sizing: border-box; margin: 0; padding: 0; }
  html, body {
    width: 1200px; height: 863px; overflow: hidden;
    background: var(--backdrop);
    font-family: "Arimo", Arial, sans-serif;
  }
  .card {
    position: absolute; left: 100px; top: 146px;
    width: 1000px; height: 571px;
    background: var(--card);
    overflow: hidden;
    box-shadow: 0 6px 18px rgba(0,0,0,0.12);
  }
  .portrait {
    position: absolute; left: 170px; bottom: 0;
    width: 330px; height: 380px;
    background: linear-gradient(180deg, var(--portrait-top) 0%, #b9a89d 35%, var(--portrait-bottom) 62%, var(--portrait-bottom) 100%);
    border-radius: 150px 150px 0 0;
  }
  .identity {
    position: absolute; right: 70px; top: 78px; text-align: right;
  }
  .identity .name {
    font-weight: 700; font-size: 34px; color: var(--maroon);
  }
  .identity .credentials {
    font-size: 19px; color: var(--maroon); font-weight: 400;
  }
  .identity .role {
    font-size: 19px; color: var(--muted-grey); margin-top: 2px;
  }
  .contact {
    position: absolute; right: 70px; top: 208px; text-align: right;
    color: var(--text-grey); font-size: 21px; line-height: 29px;
  }
  .contact .address { margin-bottom: 12px; }
  .contact .line { display: flex; justify-content: flex-end; align-items: center; gap: 9px; }
  .contact .line svg { width: 18px; height: 18px; flex: none; }
  .contact .spacer { width: 18px; flex: none; }
  .tagline-band {
    position: absolute; left: 250px; right: 0; top: 438px; height: 42px;
    background: var(--maroon-band);
    display: flex; align-items: center; justify-content: flex-end;
    padding-right: 70px;
    color: #ffffff; font-size: 20px; white-space: nowrap;
  }
</style>
</head>
<body>
  <div class="card">
    <div class="portrait" role="img" aria-label="Portrait photo of the broker in a dark suit and patterned tie"></div>

    <div class="identity">
      <p><span class="name">Dale Merrow,</span> <span class="credentials">GRI CRS ABR</span></p>
      <p class="role">Broker Owner</p>
    </div>

    <div class="contact">
      <p class="address">14637 Larkspur Ave. St.<br>Clair Shores, MI 48081</p>
      <p class="line">586-317-4902
        <svg viewBox="0 0 24 24" aria-hidden="true"><path fill="#6a1f22" d="M6.6 10.8a15 15 0 0 0 6.6 6.6l2.2-2.2a1 1 0 0 1 1-.25 11.4 11.4 0 0 0 3.6.57 1 1 0 0 1 1 1V20a1 1 0 0 1-1 1A17 17 0 0 1 3 4a1 1 0 0 1 1-1h3.5a1 1 0 0 1 1 1c0 1.25.2 2.45.57 3.57a1 1 0 0 1-.25 1z"/></svg>
      </p>
      <p class="line">dalemerrow@dalemerrowrealtors.example
        <svg viewBox="0 0 24 24" aria-hidden="true"><rect x="2" y="5" width="20" height="14" rx="1.5" fill="#6a1f22"/><path d="M3 6.5l9 6.5 9-6.5" fill="none" stroke="#f7f7f6" stroke-width="1.6"/></svg>
      </p>
      <p class="line">Licensed in Michigan &amp; Florida<span class="spacer"></span></p>
    </div>

    <div class="tagline-band">37 Years of Outstanding Service based&nbsp; on a Result Driven Marketing Plan</div>
  </div>
</body>
</html>
```